Daybreak Ledger Booklet

I have a 25 page booklet that I wrote.
I need to have a book cover design, typesetting, and imagery.
I need it to be designed with bleeds because I am having it printed.
It will be in an 8.5 X 11 format.
Please look at the 2020*.png files for an idea for the cover.
The title of the mini-book is "Daybreak Ledger" .
Subtitle is "Crestlo Method for Health and Fitness Motivation"
Then in between the title and subtitle, place the "Tobin_Health_Infographic...." image.
The other images are for inside the mini-book,
The "Daybreak-Ledger-CrestlO.pdf" file is the information in the book that will need to be typesetted.
The other images are inside the book and will need to be placed inside when appropriate.
Please don't agree to do this project if you have not done this before
I also want to see your portfolio.
Thank you
P.S. I can add all my images that are in the booklet when you accept project

Target Market(s)

Baby boomers ages 50-70

Industry/Entity Type

Fitness

Colors
0a5aa6

Requirements
Must have
• My project consists of a book cover and back. And typesetting and imagery inside the book.

```html
<!DOCTYPE html>
<html lang="en">
<head>
<meta charset="utf-8">
<title>Daybreak Ledger – Crestlo Cover</title>
<link rel="stylesheet" href="https://fonts.googleapis.com/css2?family=Oswald:wght@700&family=Roboto:ital,wght@0,300;1,700&display=swap">
<style>
  :root {
    --ink: #0a0a0a;
    --night: #1c1b1a;
    --dusk: #2e2c2a;
    --gold: #e7cd92;
    --gold-bright: #fff4d6;
    --white: #ffffff;
    --portrait: #8d8f94;
  }
  * { margin: 0; padding: 0; box-sizing: border-box; }
  html, body { width: 927px; height: 1200px; overflow: hidden; background: var(--ink); }
  .cover {
    position: relative;
    width: 927px;
    height: 1200px;
    overflow: hidden;
    background: var(--ink);
    font-family: "Roboto", Arial, sans-serif;
    color: var(--white);
  }
  .hero-photo {
    position: absolute;
    left: 0; top: 0;
    width: 927px; height: 870px;
    background:
      radial-gradient(ellipse at 50% 78%, var(--dusk) 0%, var(--night) 45%, var(--ink) 100%);
  }
  .hero-photo::after {
    content: "";
    position: absolute;
    left: 0; right: 0; bottom: 0;
    height: 120px;
    background: linear-gradient(to bottom, rgba(10,10,10,0), var(--ink));
  }
  .title-rules {
    position: absolute;
    left: 0; top: 0;
  }
  .title {
    position: absolute;
    left: 0; top: 446px;
    width: 927px;
    height: 230px;
    display: flex;
    align-items: center;
    justify-content: center;
    font-family: "Oswald", "Arial Narrow", sans-serif;
    font-weight: 700;
    font-size: 178px;
    letter-spacing: 4px;
    line-height: 1;
    color: var(--gold);
  }
  .tagline {
    position: absolute;
    left: 0; top: 770px;
    width: 927px;
    text-align: center;
    font-weight: 700;
    font-style: italic;
    font-size: 27px;
    line-height: 40px;
  }
  .promise {
    position: absolute;
    left: 120px; top: 917px;
    width: 660px;
    font-weight: 300;
    font-size: 27.5px;
    line-height: 42px;
    text-align: center;
  }
  .author-portrait {
    position: absolute;
    left: 783px; top: 922px;
    width: 102px; height: 144px;
    background: linear-gradient(160deg, #b9bbc0, var(--portrait) 55%, #3a3a3c);
  }
  .author-signature {
    position: absolute;
    left: 222px; top: 1026px;
    width: 500px; height: 80px;
    background: linear-gradient(90deg, rgba(231,205,146,0.35), rgba(231,205,146,0.12));
    border-radius: 40px;
  }
</style>
</head>
<body>
<main class="cover">
  <div class="hero-photo" role="img" aria-label="Silhouettes of two men running against a dark dusk sky"></div>

  <svg class="title-rules" width="927" height="1200" viewBox="0 0 927 1200" aria-hidden="true">
    <defs>
      <linearGradient id="rule-glow" x1="0" x2="1" y1="0" y2="0">
        <stop offset="0" stop-color="#e7cd92" stop-opacity="0"/>
        <stop offset="0.35" stop-color="#fff4d6" stop-opacity="0.9"/>
        <stop offset="0.75" stop-color="#e7cd92" stop-opacity="0.9"/>
        <stop offset="1" stop-color="#e7cd92" stop-opacity="0"/>
      </linearGradient>
    </defs>
    <rect x="70" y="440" width="810" height="4" fill="url(#rule-glow)"/>
    <rect x="40" y="679" width="800" height="4" fill="url(#rule-glow)"/>
  </svg>

  <h1 class="title">CRESTLO</h1>

  <p class="tagline">Make NOW the Time You<br>Take Your Life Back</p>

  <p class="promise">The Secrets to Finally Achieving an Elite Level of Fitness—Even If You Start at Age 63 (Like I Did)!</p>

  <div class="author-portrait" role="img" aria-label="Portrait photo of the author in sunglasses"></div>

  <div class="author-signature" role="img" aria-label="Handwritten signature of Tobin Ashford in gold"></div>
</main>
</body>
</html>
```